Bref créative
Security Company Tri-Fold Brochure
Security & Investigations
Our company provides residential and corporate security. Our Logo can be found on our website at http://examplehost.test/~pinegate/. I have detailed information about the products and services we provide
Security
Corporate, law, security
Mid-Res logo. I dont have a High res or vector version of the logo
Website content to be used in brochure

```html
<!DOCTYPE html>
<html lang="en">
<head>
<meta charset="utf-8">
<title>Pinegate Security – Tri-Fold Brochure</title>
<link rel="stylesheet" href="https://fonts.googleapis.com/css2?family=Arimo:wght@400;700&family=Tinos:wght@400;700&display=swap">
<style>
  :root{
    --backdrop:#d4d6d9;
    --navy:#17202f;
    --navy-2:#222d40;
    --steel:#4b77a6;
    --steel-light:#6f98c3;
    --steel-dark:#36597f;
    --night-1:#0d0f16;
    --night-2:#2a2a36;
    --amber:#c98f3d;
    --gold:#d8b25a;
    --white:#ffffff;
    --ink-soft:#dfe7f1;
  }
  *{box-sizing:border-box;margin:0;padding:0}
  html,body{width:1200px;height:802px;overflow:hidden}
  body{background:var(--backdrop);font-family:"Arimo",Arial,sans-serif;color:var(--white);position:relative}

  .spread{position:absolute;top:180px;width:570px;height:441px;box-shadow:0 6px 18px rgba(0,0,0,.28);overflow:hidden}
  .spread--outside{left:20px;background:var(--navy)}
  .spread--inside{left:610px;background:linear-gradient(180deg,var(--steel-light),var(--steel) 45%,var(--steel-dark))}
  .panel{position:absolute;top:0;width:190px;height:441px}
  .fold{position:absolute;top:0;width:1px;height:441px;background:rgba(0,0,0,.18)}

  /* outside — back panel */
  .back{left:0;background:var(--navy)}
  .back__head{height:20px;background:var(--steel);display:flex;align-items:center;gap:6px;padding:0 8px;font-size:7px;font-weight:700;letter-spacing:.5px}
  .dot{width:9px;height:9px;border-radius:50%;background:var(--gold);flex:none}
  .photo{position:absolute;display:block}
  .back__photo-top{left:8px;top:26px;width:174px;height:50px;background:linear-gradient(135deg,#8a6a55,#3c4a66)}
  .back__text{position:absolute;left:10px;top:84px;width:170px;font-size:6.5px;line-height:1.45;color:var(--ink-soft)}
  .back__text p{margin-bottom:7px}
  .back__photo-bottom{left:8px;top:328px;width:174px;height:60px;background:linear-gradient(135deg,#3a3a40,#6a5a4c 60%,#1f2430)}
  .back__caption{position:absolute;left:10px;top:396px;width:170px;font-size:6px;color:var(--ink-soft)}

  /* outside — cover area (two panels) */
  .skyline{left:190px;top:0;width:380px;height:262px;background:
    radial-gradient(ellipse at 35% 70%,rgba(201,143,61,.55),transparent 55%),
    radial-gradient(ellipse at 80% 85%,rgba(201,143,61,.35),transparent 50%),
    linear-gradient(180deg,var(--night-1),var(--night-2) 70%,#4a3a2e)}
  .brand{position:absolute;left:420px;top:20px;width:140px;display:flex;flex-direction:column;align-items:center;gap:6px}
  .brand__mark{width:52px;height:52px;border-radius:50%;background:var(--gold)}
  .brand__name{font-size:11px;font-weight:700;letter-spacing:1px}
  .title{position:absolute;left:410px;top:120px;width:150px;text-align:center;font-family:"Tinos","Times New Roman",serif;font-size:24px;line-height:1.05;font-weight:400;text-shadow:0 1px 3px rgba(0,0,0,.6)}
  .name-band{position:absolute;left:190px;top:164px;width:160px;height:24px;background:var(--navy-2);display:flex;align-items:center;padding-left:10px;font-size:10px;font-weight:700;letter-spacing:.6px}
  .strip{position:absolute;top:262px;height:44px;display:flex;gap:2px;left:190px;width:380px}
  .strip span{flex:1;display:block}
  .strip .s1{background:linear-gradient(135deg,#2f3b52,#7d8aa0)}
  .strip .s2{background:linear-gradient(135deg,#5a6a78,#c4b59a)}
  .strip .s3{background:linear-gradient(135deg,#1e2633,#53647c)}
  .strip .s4{background:linear-gradient(135deg,#6b7a8b,#2c3544)}
  .strip .s5{background:linear-gradient(135deg,#3a4356,#9aa5b3)}
  .cover-foot{position:absolute;left:190px;top:306px;width:380px;height:135px;background:linear-gradient(180deg,var(--steel-light),var(--steel))}
  .services{position:absolute;left:230px;top:10px;width:140px;font-size:8px;line-height:1.5}
  .services h2{font-size:8.5px;font-weight:700;margin-bottom:2px}
  .services li{list-style:none;padding-left:8px;position:relative}
  .services li::before{content:"";position:absolute;left:0;top:4px;width:4px;height:4px;background:var(--white)}
  .contact{position:absolute;left:260px;top:96px;width:110px;text-align:center;font-size:8px;line-height:1.35}
  .contact .dot{margin:0 auto 3px}
  .back-contact{position:absolute;left:20px;top:96px;width:150px;font-size:7px;line-height:1.4;color:var(--white)}

  /* inside */
  .in-col{position:absolute;top:14px;width:170px;font-size:6.5px;line-height:1.45;color:var(--white)}
  .in-col p{margin-bottom:8px}
  .in-col ul{list-style:none;margin-top:4px}
  .in-col li{padding-left:7px;position:relative}
  .in-col li::before{content:"";position:absolute;left:0;top:3px;width:3px;height:3px;background:var(--white)}
  .in-col h2{font-size:8px;font-weight:700;background:var(--navy-2);padding:3px 6px;margin-bottom:7px}
  .col-1{left:10px}
  .col-3{left:390px}
  .feature{position:absolute;left:196px;width:178px;height:70px;display:flex;gap:6px;align-items:center}
  .feature__photo{width:92px;height:62px;flex:none;display:block}
  .feature__text{font-size:6.5px;line-height:1.4}
  .feature__text .dot{margin-bottom:4px}
  .f1{top:14px}.f1 .feature__photo{background:linear-gradient(135deg,#2a3346,#8795ab)}
  .f2{top:100px}.f2 .feature__photo{background:linear-gradient(135deg,#5b5f68,#c7b79c)}
  .f3{top:186px}.f3 .feature__photo{background:linear-gradient(135deg,#1f2734,#5d6e86)}
  .in-bottom{position:absolute;left:196px;top:280px;width:178px;height:70px;background:linear-gradient(135deg,#2a3142,#6d7b92)}
  .in-foot{position:absolute;left:10px;top:380px;width:170px;height:48px;background:var(--navy-2);display:flex;align-items:center;padding:0 8px;font-size:7px;gap:6px}
</style>
</head>
<body>

<section class="spread spread--outside" aria-label="Brochure outside">
  <div class="panel back">
    <div class="back__head"><span class="dot"></span>Who We Are</div>
    <div class="photo back__photo-top" role="img" aria-label="Photo of officer at work"></div>
    <div class="back__text">
      <p>Pinegate Security delivers trained, licensed officers for residential and corporate clients. Our team works around the clock to protect people, property and assets with discretion and care.</p>
      <p>Every assignment begins with a site review and a clear plan built around your needs.</p>
    </div>
    <div class="photo back__photo-bottom" role="img" aria-label="Photo of protection agent beside vehicle"></div>
  </div>
  <div class="fold" style="left:190px"></div>

  <div class="photo skyline" role="img" aria-label="City skyline at night"></div>
  <div class="fold" style="left:380px;height:262px"></div>
  <div class="brand">
    <span class="brand__mark"></span>
    <span class="brand__name">PINEGATE</span>
  </div>
  <h1 class="title">Security<br>&amp;<br>Investigations</h1>
  <div class="name-band">PINEGATE SECURITY</div>

  <div class="strip" role="img" aria-label="Row of service photos">
    <span class="s1"></span><span class="s2"></span><span class="s3"></span><span class="s4"></span><span class="s5"></span>
  </div>

  <div class="cover-foot">
    <div class="services">
      <h2>Some of our services</h2>
      <ul>
        <li>Executive Protection</li>
        <li>Commercial &amp; Industrial</li>
        <li>Residential</li>
        <li>Investigations</li>
        <li>Alarm / Cash Logistics</li>
      </ul>
    </div>
    <div class="contact"><span class="dot"></span>Contact us<br>555.010.4827</div>
  </div>
</section>

<section class="spread spread--inside" aria-label="Brochure inside">
  <div class="in-col col-1">
    <p>Our officers are screened, trained and supervised to the highest standard. We provide uniformed and plain-clothes staff for events, offices, construction sites and private homes.</p>
    <p>We also offer patrol services, alarm response and loss prevention consulting for retail and industrial clients.</p>
    <ul>
      <li>Armed Officers</li>
      <li>Unarmed Officers</li>
      <li>Mobile Patrol</li>
      <li>Event Staff</li>
      <li>Loss Prevention</li>
    </ul>
  </div>
  <div class="in-foot" role="img" aria-label="Photo of patrol car"></div>
  <div class="fold" style="left:190px"></div>

  <div class="feature f1">
    <span class="feature__photo" role="img" aria-label="Photo of executive protection team"></span>
    <div class="feature__text"><span class="dot" style="display:block"></span>Executive protection for travel and daily routines.</div>
  </div>
  <div class="feature f2">
    <span class="feature__photo" role="img" aria-label="Photo of investigator reviewing files"></span>
    <div class="feature__text"><span class="dot" style="display:block"></span>Investigations handled by licensed professionals.</div>
  </div>
  <div class="feature f3">
    <span class="feature__photo" role="img" aria-label="Photo of secure cash transport"></span>
    <div class="feature__text"><span class="dot" style="display:block"></span>Cash logistics with secure, tracked transport.</div>
  </div>
  <div class="photo in-bottom" role="img" aria-label="Photo of officers on patrol"></div>
  <div class="fold" style="left:380px"></div>

  <div class="in-col col-3">
    <h2>Licenses</h2>
    <p>Fully licensed, bonded and insured. Our managers bring decades of experience in law enforcement and private security.</p>
    <p>Call today for a free consultation and a written proposal tailored to your property.</p>
    <ul>
      <li>Free Site Survey</li>
      <li>24/7 Dispatch</li>
      <li>Bonded &amp; Insured</li>
    </ul>
  </div>
</section>

</body>
</html>
```